Hi,

I have just started up a business called VELUMO in Melbourne. We run fun street art tours around Melbourne's CBD.

I need to create a design for the back side of my business cards. I have designed the front side (simply with my logo) however, I am having trouble designing the reverse side in a professional manner. I have attached pictures of what I have done.

The picture attached titled "VELUMO Business Cards Back" has all the information that I require on the back side of my business cards; although displayed in an amateur and simple way. As displayed in the picture, I need: the VELUMO logo, the website URL, the booking details (phone - 0481 556 217 & email - bookings@velumo.com.au) and the service description ($20, One Hour, Tours Daily, Meet at Carrow Rd Terminal). I would also like to use the font in the picture supplied which is "source-sans-pro".

The VELUMO tours are for tourists and are relaxed, entertaining and fun! I would like the design to reflect this.

Target Market(s)

Backpackers & University Students

Industry/Entity Type

Business

Requirements
Must have
• The VELUMO logo, the website URL, the booking details (phone - 0481 556 217 & email - bookings@velumo.com.au) and the service description ($20, One Hour, Tours Daily, Meet at Carrow Rd Terminal).

```html
<!DOCTYPE html>
<html lang="en">
<head>
<meta charset="utf-8">
<title>VELUMO Business Card Back</title>
<link rel="stylesheet" href="https://fonts.googleapis.com/css2?family=Josefin+Sans:wght@400;600;700&display=swap">
<style>
  :root {
    --bg-deep: #2a0404;
    --bg-mid: #7a0c0f;
    --bg-bright: #e8282c;
    --band-dark: rgba(40, 2, 2, 0.45);
    --band-light: rgba(255, 80, 70, 0.10);
    --accent: #ff5a48;
    --accent-soft: #ff7a68;
    --tag: #e8232b;
    --tag-text: #ffffff;
    --panel: rgba(255, 70, 60, 0.16);
    --logo-ink: #1a0202;
    --logo-field: #ff5b4e;
  }
  * { box-sizing: border-box; margin: 0; padding: 0; }
  html, body { width: 1200px; height: 777px; overflow: hidden; background: var(--bg-deep); }
  .card {
    position: relative;
    width: 1200px;
    height: 777px;
    overflow: hidden;
    font-family: "Josefin Sans", sans-serif;
    background:
      radial-gradient(ellipse 700px 520px at 1060px 150px, var(--bg-bright) 0%, rgba(200,30,34,0.6) 45%, transparent 80%),
      linear-gradient(100deg, var(--bg-deep) 0%, var(--bg-mid) 55%, #b3171b 100%);
  }
  .band-top { position: absolute; left: 0; top: 0; width: 100%; height: 45px; background: var(--band-dark); }
  .band-header { position: absolute; left: 0; top: 45px; width: 100%; height: 208px; background: var(--band-light); }
  .band-bottom { position: absolute; left: 0; top: 747px; width: 100%; height: 30px; background: var(--band-dark); }

  .logo {
    position: absolute;
    left: 330px; top: 100px;
    width: 540px; height: 130px;
    display: flex; align-items: center; justify-content: center;
  }
  .logo-mark {
    width: 26px; height: 26px; border-radius: 50%;
    background: var(--logo-field); margin-right: 18px;
  }
  .logo-name {
    font-weight: 700; font-size: 92px; letter-spacing: 4px;
    color: var(--logo-ink); line-height: 1; padding-top: 14px;
  }

  .website {
    position: absolute;
    left: 409px; top: 253px; width: 359px; height: 53px;
    background: rgba(190, 25, 28, 0.75);
    color: var(--accent-soft);
    font-size: 31px; font-weight: 600;
    display: flex; align-items: center; justify-content: center;
    padding-top: 6px;
  }

  .booking {
    position: absolute;
    left: 48px; top: 415px; width: 481px; height: 193px;
    background: var(--panel);
    color: var(--accent);
    text-align: center;
    padding-top: 30px;
  }
  .booking-cta { font-size: 31px; font-variant: small-caps; font-weight: 400; line-height: 1.1; }
  .booking-phone { font-size: 56px; font-weight: 400; line-height: 1.05; letter-spacing: 1px; margin-top: 2px; }
  .booking-email { font-size: 32px; font-weight: 400; line-height: 1.1; margin-top: 2px; }

  .detail { position: absolute; right: 20px; display: flex; align-items: center; }
  .detail-label {
    color: var(--accent); font-size: 26px; font-weight: 400;
    transform: rotate(-9deg); text-align: right; line-height: 1;
    margin-right: 10px;
  }
  .detail-dot { width: 12px; height: 12px; border-radius: 50%; background: var(--accent); margin-right: 12px; }
  .detail-tag {
    height: 62px;
    background: var(--tag);
    color: var(--tag-text);
    font-size: 44px; font-weight: 400;
    display: flex; align-items: center; justify-content: flex-end;
    padding: 8px 18px 0 46px;
    clip-path: polygon(0 50%, 34px 0, 100% 0, 100% 100%, 34px 100%);
  }
  .detail-rate { top: 380px; }
  .detail-rate .detail-tag { width: 158px; }
  .detail-length { top: 462px; }
  .detail-length .detail-tag { width: 266px; }
  .detail-when { top: 543px; }
  .detail-when .detail-tag { width: 362px; }
  .detail-where { top: 625px; }
  .detail-where .detail-tag { width: 449px; font-size: 42px; }
  .detail-where .detail-label { font-size: 24px; }
</style>
</head>
<body>
<main class="card">
  <div class="band-top"></div>
  <div class="band-header"></div>
  <div class="band-bottom"></div>

  <header class="logo">
    <span class="logo-mark"></span>
    <span class="logo-name">VELUMO</span>
  </header>

  <div class="website">www.velumo.com.au</div>

  <section class="booking">
    <p class="booking-cta">Call KAI to Book Now</p>
    <p class="booking-phone">0481 556 217</p>
    <p class="booking-email">bookings@velumo.com.au</p>
  </section>

  <div class="detail detail-rate">
    <span class="detail-label">Rate?</span>
    <span class="detail-dot"></span>
    <span class="detail-tag">$20</span>
  </div>
  <div class="detail detail-length">
    <span class="detail-label">For?</span>
    <span class="detail-dot"></span>
    <span class="detail-tag">One Hour</span>
  </div>
  <div class="detail detail-when">
    <span class="detail-label">When?</span>
    <span class="detail-dot"></span>
    <span class="detail-tag">Tours Daily</span>
  </div>
  <div class="detail detail-where">
    <span class="detail-label">Where Should<br>I Meet?</span>
    <span class="detail-dot"></span>
    <span class="detail-tag">Carrow Rd Terminal</span>
  </div>
</main>
</body>
</html>
```